Prepared Meal Delivery Website

Need a new modern design for a prepared meal delivery company that is hosted on Shopify.

Target Market(s)

Young Professionals

Industry/Entity Type

Prepared Meal Delivery Service

Number of Pages Required

5+ page

Requirements
Must have
• Use https://www.vorabelmeals.com/ as an example
Nice to have
• Vibrant page with call to action obvious and repeated
Should not have
• Generic look, grays/white/black

```html
<!DOCTYPE html>
<html lang="en">
<head>
<meta charset="utf-8">
<title>Dash Table Meals</title>
<link href="https://fonts.googleapis.com/css2?family=Manrope:wght@400;500;600;700&display=swap" rel="stylesheet">
<style>
:root{
  --orange:#e46f0a;
  --ink:#2a221c;
  --text:#4a4a4a;
  --dark:#141312;
  --darker:#0d0c0b;
  --cream:#fff7ec;
  --topbar:#2b2420;
  --white:#ffffff;
}
*{box-sizing:border-box;margin:0;padding:0}
html,body{width:1200px;height:3151px;overflow:hidden}
body{font-family:'Manrope',sans-serif;color:var(--ink);background:var(--white);position:relative}
.abs{position:absolute}
.btn{position:absolute;display:flex;align-items:center;justify-content:center;background:var(--orange);color:var(--white);border-radius:10px;font-size:18px;font-weight:500;text-decoration:none}
.eyebrow{color:var(--orange);font-size:17px;font-weight:600;letter-spacing:2.5px;text-transform:uppercase}
.photo{position:absolute}

.topbar{top:0;left:0;width:1200px;height:41px;background:var(--topbar);color:var(--white);font-size:15px}
.topbar .phone{left:104px;top:11px}
.topbar .note{left:383px;top:11px}
.topbar .note u{font-weight:600}
.topbar .social{right:104px;top:12px;display:flex;gap:13px}
.topbar .social span{width:16px;height:16px;border-radius:3px;background:var(--white);opacity:.9}

.nav{top:41px;left:0;width:1200px;height:118px;background:var(--white);border-bottom:1px solid #ddd}
.brand{left:104px;top:34px;width:169px;height:50px;border:2px solid var(--ink);display:flex;align-items:center;justify-content:center;font-size:15px;font-weight:600;letter-spacing:3px;text-transform:uppercase}
.nav ul{list-style:none;display:flex;gap:30px;left:315px;top:49px;font-size:17px;font-weight:500}
.nav .btn{left:948px;top:28px;width:148px;height:64px}

.hero{top:159px;left:0;width:1200px;height:422px;background:linear-gradient(90deg,#f3f1ef 0%,#f7f6f4 45%,#dcd8d0 60%,#8b9a5d 75%,#3f5a2c 90%,#c8bfb2 100%)}
.hero h1{left:138px;top:70px;font-size:50px;line-height:46px;font-weight:700;letter-spacing:-.5px}
.hero p{left:138px;top:192px;width:430px;font-size:17px;line-height:24px;color:var(--text)}
.hero .btn{left:138px;top:290px;width:148px;height:64px}

.menu{top:581px;left:0;width:1200px;height:649px}
.menu .eyebrow{top:32px;width:1200px;text-align:center}
.menu h2{top:56px;width:1200px;text-align:center;font-size:33px;font-weight:600}
.card{position:absolute;top:116px;width:317px}
.card .photo{position:relative;width:317px;height:306px;border-radius:10px}
.card h3{margin-top:22px;font-size:19px;font-weight:600}
.card p{margin-top:14px;font-size:17px;line-height:24px;color:var(--text);width:270px}
.menu .btn{left:508px;top:558px;width:185px;height:64px}

.how{top:1230px;left:0;width:1200px;height:430px;background:var(--cream)}
.how .eyebrow{top:50px;width:1200px;text-align:center}
.how h2{top:74px;width:1200px;text-align:center;font-size:32px;font-weight:600}
.step{position:absolute;top:193px;width:170px;text-align:center;font-size:17px;line-height:23px;color:var(--text)}
.step .icon{width:100px;height:100px;margin:0 auto 48px;border-radius:50%;background:linear-gradient(135deg,#f7c3a0,#e46f0a 60%,#2a221c)}
.step.final{color:var(--orange);font-size:18px;line-height:19px}
.step.final .icon{box-shadow:0 0 60px 30px #fde9b0}

.kits{top:1660px;left:0;width:1200px;height:744px}
.kits .eyebrow{left:104px;top:40px}
.kits h2{left:104px;top:66px;font-size:33px;line-height:34px;font-weight:600}
.kits p{left:104px;top:158px;width:575px;font-size:17px;line-height:24px;color:var(--text)}
.kits .btn{left:104px;top:357px;width:178px;height:64px}

.help{top:2404px;left:0;width:1200px;height:393px;background:var(--dark)}
.help h2{left:583px;top:80px;font-size:31px;line-height:30px;font-weight:600;color:var(--white)}
.help p{left:583px;top:168px;width:420px;font-size:17px;line-height:24px;color:var(--white)}
.help .btn{top:244px;width:178px;height:64px}
.help .btn.light{background:var(--white);color:var(--ink)}

.footer{top:2797px;left:0;width:1200px;height:304px;background:var(--dark);color:var(--white)}
.footer .mark{left:88px;top:48px;width:122px;height:122px;border:2px solid var(--white);border-radius:50%;display:flex;align-items:center;justify-content:center;text-align:center;font-size:12px;font-weight:600;letter-spacing:2px;line-height:17px}
.footer .about{left:88px;top:192px;width:240px;font-size:17px;line-height:22px}
.footer h4{color:var(--orange);font-size:19px;font-weight:600}
.footer ul{list-style:none;margin-top:14px;font-size:16px;line-height:37px}
.footer .news p{margin-top:12px;width:270px;font-size:16px;line-height:21px}
.footer .email{left:844px;top:168px;width:272px;height:48px;border-radius:24px;background:#1e1d1b;color:#777;font-size:16px;display:flex;align-items:center;justify-content:center}
.footer .submit{left:844px;top:226px;width:272px;height:46px;border-radius:23px;background:var(--orange);font-size:17px;font-weight:500;display:flex;align-items:center;justify-content:center;gap:10px}

.bottom{top:3101px;left:0;width:1200px;height:50px;background:var(--darker);color:#9a9a9a;font-size:15px}
.bottom .copy{left:82px;top:16px}
.bottom .social{right:82px;top:14px;display:flex;gap:18px}
.bottom .social span{width:20px;height:20px;border:1.5px solid #9a9a9a;border-radius:5px}
</style>
</head>
<body>

<div class="abs topbar">
  <div class="abs phone">(490) 555-0148</div>
  <div class="abs note">Lorem ipsum dolor sit amet, consectetur &nbsp;-&nbsp; <u>adipiscing elit.</u></div>
  <div class="abs social"><span></span><span></span><span></span><span></span></div>
</div>

<header class="abs nav">
  <div class="abs brand">Dash Table</div>
  <ul class="abs"><li>Our Menu</li><li>How it works</li><li>About</li><li>FAQ</li></ul>
  <a class="btn">Get Started</a>
</header>

<section class="abs hero">
  <div class="photo" role="img" aria-label="Fresh green salad with tofu, onion and chickpeas in a white bowl" style="left:0;top:0;width:1200px;height:422px"></div>
  <h1 class="abs">The meal kit that<br>puts quality first</h1>
  <p class="abs">Lorem ipsum dolor sit amet, consectetur adipiscing elit. Tempus sit egestas a, et ante urna, in pellentesque nunc.</p>
  <a class="btn">Order Meal</a>
</section>

<section class="abs menu">
  <div class="abs eyebrow">Our Menu</div>
  <h2 class="abs">10+ Million meals shipped</h2>
  <div class="card" style="left:104px">
    <div class="photo" role="img" aria-label="Grilled steak with sweet potato wedges and rosemary in a skillet" style="background:linear-gradient(135deg,#5a4130,#2a211b 50%,#a0522d)"></div>
    <h3>Lorem ipsum dolor sit amet</h3>
    <p>Our chefs bring high standards to crafting your meals.</p>
  </div>
  <div class="card" style="left:442px">
    <div class="photo" role="img" aria-label="Assorted sushi rolls and nigiri on a wooden boat" style="background:linear-gradient(135deg,#8a6a4a,#d9b48c 50%,#3b3a36)"></div>
    <h3>Lorem ipsum dolor sit amet</h3>
    <p>80% of ingredients come directly from producers.</p>
  </div>
  <div class="card" style="left:779px">
    <div class="photo" role="img" aria-label="Seafood pasta with clams and lemon on a blue plate" style="background:linear-gradient(135deg,#3b2418,#9fb3b8 50%,#c0733a)"></div>
    <h3>Lorem ipsum dolor sit amet</h3>
    <p>Get boxes on your schedule. Skip, pause, or cancel anytime.</p>
  </div>
  <a class="btn">View Full Menu</a>
</section>

<section class="abs how">
  <div class="abs eyebrow">How it works</div>
  <h2 class="abs">See how we graciously process your food!</h2>
  <svg class="abs" style="left:0;top:0" width="1200" height="430" fill="none" stroke="#f0a868" stroke-width="3" stroke-dasharray="10 7">
    <path d="M238 234 Q300 214 355 234"/>
    <path d="M452 252 Q510 262 552 250"/>
    <path d="M666 224 Q720 224 760 238"/>
    <path d="M878 256 Q920 254 955 240"/>
  </svg>
  <div class="step" style="left:96px"><div class="icon" role="img" aria-label="Phone with meal cloche icon"></div>You choose your perfect meal</div>
  <div class="step" style="left:310px"><div class="icon" role="img" aria-label="Support agent icon"></div>We confirm the order</div>
  <div class="step" style="left:524px"><div class="icon" role="img" aria-label="Hand holding approved package icon"></div>Order being processed within minutes</div>
  <div class="step" style="left:729px"><div class="icon" role="img" aria-label="Delivery scooter icon"></div>Order on the way to you</div>
  <div class="step final" style="left:933px"><div class="icon" role="img" aria-label="Door with delivered meal icon"></div>Knock knock,<br>Order's Here!</div>
</section>

<section class="abs kits">
  <div class="abs eyebrow">Best Meal Kits</div>
  <h2 class="abs">Lorem ipsum dolor sit amet<br>elit Dash Table Meals</h2>
  <p class="abs">Lorem ipsum dolor sit amet, consectetur adipiscing elit. Sit elementum gravida malesuada facilisis suspendisse egestas mi, etiam magna. Proin tellus et amet eget. Nulla nunc lorem semper sodales hac eu diam. Eget mauris id purus consectetur donec. Tortor laoreet maecenas faucibus sed leo. Nullam hendrerit consectetur lectus amet id sed dui. Integer pellentesque quis a non consequat ut lorem nullam. Elementum risus dictum in augue sem sagittis cursus.</p>
  <a class="btn">Meal Kits</a>
  <div class="photo" role="img" aria-label="Sliced roast beef with grilled peppers and gravy boat on a wooden board" style="left:741px;top:34px;width:355px;height:426px;background:linear-gradient(160deg,#e9e6df 0%,#8a5a32 40%,#c0392b 65%,#e0a020 80%,#6a4020)"></div>
  <div class="photo" role="img" aria-label="Plate of avocado, egg and greens with toast" style="left:108px;top:460px;width:194px;height:248px;background:linear-gradient(135deg,#5b6e94,#e8e4dc 50%,#6a8a3a)"></div>
  <div class="photo" role="img" aria-label="Roast chicken with potatoes and carrots" style="left:302px;top:460px;width:204px;height:248px;background:linear-gradient(135deg,#1e3340,#d9a53a 50%,#b5682a)"></div>
  <div class="photo" role="img" aria-label="Herb roasted meat on a wooden board" style="left:506px;top:460px;width:296px;height:248px;background:linear-gradient(135deg,#e8c88a,#6a3a1e 50%,#2a1c14)"></div>
  <div class="photo" role="img" aria-label="Bowl of roasted chickpeas" style="left:802px;top:460px;width:99px;height:248px;background:linear-gradient(180deg,#2e2a26,#b08a3a)"></div>
  <div class="photo" role="img" aria-label="Stir fried beef with vegetables in a dark bowl" style="left:901px;top:460px;width:195px;height:248px;background:linear-gradient(135deg,#4a5058,#a03020 50%,#2a2420)"></div>
</section>

<section class="abs help">
  <div class="photo" role="img" aria-label="Noodle soup bowl with chopsticks among dishes on a dark table" style="left:0;top:0;width:1200px;height:393px;background:radial-gradient(circle at 240px 200px,#e0a820 0,#7a3a18 120px,#3a2a20 230px,#141312 560px)"></div>
  <h2 class="abs">Need help?<br>Contact us to get support</h2>
  <p class="abs">Lorem ipsum dolor sit amet, consectetur adipiscing elit. Sit elementum gravida malesuad</p>
  <a class="btn" style="left:583px">Contact us</a>
  <a class="btn light" style="left:776px">FAQs</a>
</section>

<footer class="abs footer">
  <div class="abs mark">DASH<br>TABLE</div>
  <p class="abs about">Lorem ipsum dolor sit amet, consectetur adipiscing elit</p>
  <div class="abs" style="left:460px;top:56px"><h4>Our Company</h4><ul><li>Our Menu</li><li>Menu Kits</li><li>How it works</li><li>Order Now</li></ul></div>
  <div class="abs" style="left:695px;top:56px"><h4>About</h4><ul><li>Support</li><li>Contact</li><li>Terms</li><li>Blog</li></ul></div>
  <div class="abs news" style="left:850px;top:56px"><h4>Subscribe to our Newsletter</h4><p>Lorem ipsum dolor sit amet, consectetur adipiscing elit, sed do eiusmod</p></div>
  <div class="abs email">Enter email address</div>
  <div class="abs submit">Submit
    <svg width="18" height="14" viewBox="0 0 18 14" fill="none" stroke="#fff" stroke-width="2"><path d="M1 7h15M10 1l6 6-6 6"/></svg>
  </div>
</footer>

<div class="abs bottom">
  <div class="abs copy">Copyright © 2022</div>
  <div class="abs social"><span></span><span></span><span></span><span></span></div>
</div>

</body>
</html>
```